Brochure - Capabilities Statement doc - 1 page handout

I would like to upgrade our "capabilities statement" brochure doc to look more professional and designed with a tailored modern look. see attached document for details. We use this document when we are in meetings or when we introduce our company in an email to a new prospect client. Its a one page overview of the services we provide. At the moment it is a terrible juvenile looking doc. with no thought to design. I am hoping you can change that and help capture our customers attention when they read it.

Target Market(s)

Our client base is corporations, tech companies and non-profits

Industry/Entity Type

It Professional

Font styles to use
Sans Serif

Requirements
Must have
• I'd like a cleaver sharp look to it. Not just columns and bullet points like I have now. This will be emailed to clients in a pdf and I'd like to have a hand out when in meetings.

```html
<!DOCTYPE html>
<html lang="en">
<head>
<meta charset="utf-8">
<title>Capabilities Statement</title>
<link href="https://fonts.googleapis.com/css2?family=Montserrat:wght@300;400;600;700&display=swap" rel="stylesheet">
<style>
  :root{
    --orange:#ee8322;
    --orange-dark:#d9691a;
    --ink:#4a4a4a;
    --muted:#666;
    --white:#ffffff;
    --band:#f1f1f1;
    --rule:#9a9a9a;
  }
  *{margin:0;padding:0;box-sizing:border-box}
  html,body{width:960px;height:1200px;overflow:hidden;background:#fff}
  body{font-family:'Montserrat',sans-serif;color:var(--ink)}
  .sheet{position:relative;width:960px;height:1200px;overflow:hidden;background:var(--white)}
  .shapes{position:absolute;inset:0}
  .brand{position:absolute;left:538px;top:28px;width:152px;height:152px;display:flex;align-items:center;justify-content:center;text-align:center;color:var(--white);font-weight:700;font-size:17px;line-height:1.2}
  .title{position:absolute;left:32px;top:84px;font-weight:700;color:var(--orange);font-size:37px;line-height:45px;letter-spacing:.5px}
  .intro{position:absolute;left:32px;top:203px;color:var(--white);font-weight:300;font-size:15px;line-height:18.6px}
  .intro .line{display:block;white-space:nowrap}
  .intro p+p{margin-top:18.6px}
  h2{position:absolute;font-weight:600;color:var(--orange);font-size:20px;letter-spacing:.5px}
  .checks{position:absolute;list-style:none;font-weight:300;font-size:15.2px;color:var(--ink)}
  .checks li{position:relative;padding-left:24px;line-height:17px}
  .checks li::before{content:"";position:absolute;left:0;top:2px;width:13px;height:13px;border:1.6px solid var(--orange)}
  .checks li::after{content:"";position:absolute;left:5px;top:-2px;width:6px;height:12px;border-right:2px solid var(--orange);border-bottom:2px solid var(--orange);transform:rotate(40deg)}
  .caps{left:44px;top:547px}
  .caps li{margin-bottom:7.3px}
  .highlights{left:45px;top:942px}
  .highlights li{margin-bottom:7.3px}
  .different{left:566px;top:566px}
  .different li{margin-bottom:13.5px;line-height:15px}
  .partners{left:566px;top:756px}
  .partners li{margin-bottom:7.3px;padding-left:29px}
  .codes{position:absolute;left:555px;font-size:12.5px;font-weight:400;color:var(--muted)}
  .footer-label{position:absolute;left:32px;top:1151px;color:var(--white);font-weight:600;font-size:15.5px;letter-spacing:.3px}
</style>
</head>
<body>
<main class="sheet">
  <svg class="shapes" width="960" height="1200" viewBox="0 0 960 1200">
    <defs>
      <linearGradient id="venueGlow" x1="0" y1="0" x2="1" y2="1">
        <stop offset="0" stop-color="#a8401c"/>
        <stop offset=".5" stop-color="#d8742e"/>
        <stop offset="1" stop-color="#6d3a28"/>
      </linearGradient>
      <linearGradient id="eventTiles" x1="0" y1="0" x2="1" y2="1">
        <stop offset="0" stop-color="#7a6a5e"/>
        <stop offset=".5" stop-color="#c9b8a6"/>
        <stop offset="1" stop-color="#8a5a3c"/>
      </linearGradient>
    </defs>
    <polygon class="top-tab" points="0,0 283,0 328,59 0,59" fill="var(--orange)"/>
    <polygon class="intro-block" points="0,182 430,182 676,487 0,487" fill="var(--orange)"/>
    <polygon role="img" aria-label="Photo of a conference audience in a warm-lit hall" points="355,0 960,0 960,365 767,528 579,332" fill="url(#venueGlow)"/>
    <polygon class="corner-accent" points="960,373 889,440 960,523" fill="var(--orange)"/>
    <g role="img" aria-label="Photo tiles of a speaker, networking guests, banquet tables and a seated audience">
      <polygon points="780,177 948,368 767,528 579,332" fill="url(#eventTiles)" stroke="#fff" stroke-width="6"/>
      <line x1="673" y1="254" x2="857" y2="448" stroke="#fff" stroke-width="5"/>
      <line x1="864" y1="272" x2="673" y2="430" stroke="#fff" stroke-width="5"/>
    </g>
    <circle cx="614" cy="104" r="76" fill="var(--orange)" stroke="#fff" stroke-width="4"/>
    <rect class="footer-band" x="0" y="1125" width="960" height="75" fill="var(--band)"/>
    <polygon class="footer-tab" points="0,1143 350,1143 362,1162 350,1181 0,1181" fill="var(--orange)"/>
    <g class="badges">
      <circle cx="438" cy="1163" r="28" fill="#1f3f7a"/>
      <line x1="504" y1="1145" x2="504" y2="1181" stroke="var(--rule)"/>
      <rect x="542" y="1141" width="108" height="44" rx="4" fill="#fff" stroke="#1f6d73" stroke-width="2"/>
      <line x1="683" y1="1145" x2="683" y2="1181" stroke="var(--rule)"/>
      <circle cx="754" cy="1163" r="22" fill="none" stroke="#8aa0b8" stroke-width="3"/>
      <line x1="822" y1="1145" x2="822" y2="1181" stroke="var(--rule)"/>
      <circle cx="856" cy="1163" r="18" fill="#111"/>
      <rect x="880" y="1150" width="50" height="26" fill="#222"/>
    </g>
  </svg>

  <div class="brand">Summit<br>Bridge<br>Events</div>

  <h1 class="title">CAPABILITIES<br>STATEMENT</h1>

  <div class="intro">
    <p>
      <span class="line">Summit Bridge Events is a meeting, event and</span>
      <span class="line">project management services company. We</span>
      <span class="line">specialize in capturing your ideas, objectives and</span>
      <span class="line">budget and transforming them into an unforgettable</span>
      <span class="line">experience.</span>
    </p>
    <p>
      <span class="line">Summit Bridge Events has been in business for over 18 years</span>
      <span class="line">and has amassed over 130 years of combined staff</span>
      <span class="line">experience. Our expertise includes customized online</span>
      <span class="line">registration software, destination selection as well as housing and</span>
      <span class="line">onsite management. Our ability to leverage our buying power and</span>
      <span class="line">excellent reputation, ensures that our clients procure the best value</span>
      <span class="line">and service for their investment.</span>
      <span class="line">Summit Bridge Events successfully executes over 150 events annually.</span>
    </p>
  </div>

  <h2 style="left:32px;top:508px">CAPABILITIES</h2>
  <ul class="checks caps">
    <li>Site Research and Hotel &amp; Venue Contract Negotiations</li>
    <li>Customized Registration Software &amp; Management</li>
    <li>City-wide Housing Management</li>
    <li>Destination Management Services</li>
    <li>Group Transportation Services</li>
    <li>Airport Meet &amp; Greet Services</li>
    <li>Project Management</li>
    <li>Meeting Management</li>
    <li>Event Management</li>
    <li>Special Event Coordination</li>
    <li>Custom Tours and Activities</li>
    <li>Showroom Installation Services</li>
    <li>Onsite Staff Services / Registration Desk Services<br>&amp; Software</li>
  </ul>

  <h2 style="left:33px;top:902px">HIGHLIGHTS</h2>
  <ul class="checks highlights">
    <li>There is no request too large or too small</li>
    <li>Tested and approved suppliers and<br>vendor partnerships</li>
    <li>A-la-carte proposals and services</li>
    <li>Creative experienced team</li>
    <li>We guarantee our work</li>
    <li>We pre-quote the job and honor the quote!</li>
  </ul>

  <h2 style="left:555px;top:530px">WHAT MAKES US DIFFERENT?</h2>
  <ul class="checks different">
    <li>Certified Meeting Professionals (CMP)</li>
    <li>WOBE Certified</li>
    <li>Local, National and International services</li>
    <li>Long-standing client retention through<br>successful partnerships</li>
  </ul>

  <h2 style="left:555px;top:716px">OUR PARTNERS:</h2>
  <ul class="checks partners">
    <li>Top 500 Companies</li>
    <li>Consumer Packaged Goods Industry</li>
    <li>Manufacturing</li>
    <li>Organizations</li>
    <li>Technology Industry</li>
    <li>Non-profit Organizations</li>
    <li>Colleges and Universities</li>
    <li>Client references upon request</li>
  </ul>

  <h2 style="left:555px;top:973px">NAICS CODES:</h2>
  <div class="codes" style="top:1004px">561599 &nbsp;&nbsp;|&nbsp;&nbsp; 561920</div>

  <h2 style="left:555px;top:1047px">UNSPSC CODES:</h2>
  <div class="codes" style="top:1075px">80141607</div>

  <div class="footer-label">CERTIFICATIONS AND ASSOCIATIONS</div>
</main>
</body>
</html>
```